Craft a new attractive & professional PowerPoint presentation based on the material provided

Dear Designer,
We are looking for a fresh revamp of our Corporate Power Point presentation. Please find attached:
- the current ppt file;
- new pdf with Corporate profile;
- our logo.
For more information please consult our Social Media Channels:
LinkedIn: https://www.linkedin.com/company/7416092/admin/
IG: https://www.instagram.com/korvalbristle/
YT: https://www.youtube.com/channel/UCmQaRtZoPeWnKxLbVdTyrfa
Deadline: before November 20th 2022.
Please do not hesitate to reach out for any questions.
Best wishes,
KVL Marketing Team
Font styles to use
Other font styles liked:
- Helvetica types
Colors
Designer to choose colors to be used in the design.
Look and feel
Each slider illustrates characteristics of the customer's brand and the style your logo design should communicate.

```html
<!DOCTYPE html>
<html lang="en">
<head>
<meta charset="utf-8">
<title>KVL Corporate Presentation</title>
<link href="https://fonts.googleapis.com/css2?family=Oswald:wght@500;700&family=Raleway:wght@300;400;600&family=Arimo:wght@400;700&display=swap" rel="stylesheet">
<style>
  :root{
    --board:#bdbec1;
    --red:#d10a11;
    --red-dark:#b8080e;
    --grey-title:#8a8a8a;
    --ink:#333;
    --line:#9a9a9a;
    --white:#fff;
  }
  *{margin:0;padding:0;box-sizing:border-box}
  html,body{width:1200px;height:800px;overflow:hidden;background:var(--board)}
  .board{position:relative;width:1200px;height:800px}
  .slide{position:absolute;width:534px;height:301px;background:var(--white);overflow:hidden;box-shadow:0 6px 14px rgba(0,0,0,.18)}
  .slide--cover{left:42px;top:70px;background:linear-gradient(180deg,#a9a9a9 0%,#f4f4f4 55%,#ededed 80%,#b9b9b9 100%)}
  .slide--family{left:619px;top:70px}
  .slide--heritage{left:42px;top:432px}
  .slide--world{left:618px;top:432px}

  .brand{position:absolute;display:flex;align-items:center;gap:3px;font-family:'Arimo',sans-serif;font-weight:700;color:var(--red);font-size:14px}
  .brand__mark{width:10px;height:10px;background:var(--red)}
  .slide--cover .brand{left:16px;top:14px}
  .slide-header .brand{right:14px;top:12px}

  .cover__title{position:absolute;left:16px;top:108px;font-family:'Oswald',sans-serif;font-weight:700;font-size:37px;line-height:44px;letter-spacing:.3px}
  .cover__title .red{color:var(--red);display:block}
  .cover__title .grey{color:#7c7c7c;display:block}
  .cover__tagline{position:absolute;left:20px;top:195px;font-family:'Arimo',sans-serif;font-weight:700;font-size:8.5px;color:var(--red)}
  .url{position:absolute;font-family:'Raleway',sans-serif;font-size:8.5px;color:var(--red)}
  .slide--cover .url{left:16px;top:279px}
  .cover__art{position:absolute;left:0;top:0}

  .slide-header__title{position:absolute;left:20px;top:12px;font-family:'Oswald',sans-serif;font-weight:700;font-size:15px;letter-spacing:.2px}
  .slide-header__title .red{color:var(--red)}
  .slide-header__title .grey{color:var(--grey-title)}
  .slide-header__rule{position:absolute;left:20px;top:34px;width:448px;height:1px;background:var(--line)}

  .family__intro{position:absolute;left:20px;top:48px;width:448px;font-family:'Raleway',sans-serif;font-size:10.2px;line-height:11px;color:var(--red);text-align:justify;text-align-last:left}
  .family__intro strong{font-weight:600}
  .family__band{position:absolute;left:0;top:92px;width:534px;height:3px;background:var(--red)}
  .family__photo{position:absolute;left:0;top:95px;width:534px;height:206px;background:linear-gradient(180deg,#7e9fc4 0%,#c9b08c 35%,#b99d77 55%,#6a6d66 72%,#8c8d89 100%)}
  .family__footer{position:absolute;left:0;top:276px;width:534px;height:12px}
  .family__footer .tab{position:absolute;left:0;top:1px;width:12px;height:8px;background:var(--white);border-radius:0 4px 4px 0}
  .family__footer .url{left:24px;top:0;color:var(--white);font-size:6px}
  .family__footer .rule{position:absolute;left:94px;top:5px;width:440px;height:1px;background:rgba(255,255,255,.8)}

  .slide-footer{position:absolute;left:0;top:278px;width:534px;height:12px}
  .slide-footer .tab{position:absolute;left:0;top:1px;width:13px;height:8px;background:var(--red);border-radius:0 4px 4px 0}
  .slide-footer .url{left:24px;top:0;font-size:6px}
  .slide-footer .rule{position:absolute;left:93px;top:5px;width:441px;height:1px;background:var(--red)}

  .heritage__map{position:absolute;left:60px;top:50px;width:430px;height:210px;background:radial-gradient(ellipse at center,#f1f1f1 0%,#fafafa 60%,#fff 100%)}
  .timeline{position:absolute;left:0;top:0}
  .year{font-family:'Arimo',sans-serif;font-weight:700;font-size:12px;fill:var(--red)}
  .milestone{position:absolute;display:flex;align-items:center;justify-content:center;transform:translateX(-50%)}
  .milestone__photo{width:65px;height:35px;border-radius:3px;background:linear-gradient(135deg,#6b5540,#a08868)}
  .milestone__brushes{width:36px;height:45px;border-radius:4px;background:linear-gradient(180deg,#e9dca0,#f4ecc4)}
  .milestone__name{font-family:'Arimo',sans-serif;font-weight:700;color:var(--red);font-size:13px;gap:3px}
  .milestone__name .sq{width:9px;height:9px;background:var(--red)}
  .milestone__partner{font-family:'Arimo',sans-serif;font-weight:700;color:#444;font-size:12px;letter-spacing:.5px}
  .milestone__badge-blue{width:32px;height:32px;border-radius:3px;background:#1c4f9c}
  .milestone__badge-ring{width:38px;height:38px;border-radius:50%;border:3px solid var(--red)}
  .milestone__ready{font-family:'Arimo',sans-serif;font-weight:700;color:var(--red);font-size:9.5px;line-height:12px;text-align:center;width:70px}

  .facts{position:absolute;left:10px;top:88px;list-style:none}
  .fact{position:relative;height:26px;margin-bottom:21px;display:flex;align-items:center}
  .fact__check{position:relative;z-index:2;width:28px;height:28px;border-radius:50%;background:var(--white);box-shadow:0 0 0 3px #f0f0f0;display:flex;align-items:center;justify-content:center}
  .fact__check span{width:22px;height:22px;border-radius:50%;background:var(--red);display:flex;align-items:center;justify-content:center}
  .fact__pill{margin-left:-14px;height:26px;width:206px;padding-left:22px;background:var(--red);border-radius:0 13px 13px 0;display:flex;align-items:center;font-family:'Raleway',sans-serif;font-size:8.3px;color:var(--white)}
  .world__map{position:absolute;left:268px;top:90px;width:230px;height:125px;border-radius:40% 45% 35% 40%;background:radial-gradient(ellipse at center,#c4c4c4 0%,#d8d8d8 55%,#fff 75%)}
</style>
</head>
<body>
<main class="board">

  <section class="slide slide--cover">
    <svg class="cover__art" width="534" height="301" viewBox="0 0 534 301">
      <defs>
        <radialGradient id="brushTones" cx="50%" cy="50%" r="60%">
          <stop offset="0" stop-color="#6f7f8e"/>
          <stop offset=".55" stop-color="#8a7b6a"/>
          <stop offset="1" stop-color="#5a5048"/>
        </radialGradient>
      </defs>
      <circle cx="448" cy="206" r="168" fill="none" stroke="var(--red)" stroke-width="1.2"/>
      <circle cx="448" cy="206" r="160" fill="url(#brushTones)" role="img" aria-label="Photo of hands holding a set of wire wheel brushes"/>
      <path d="M258,167 A190,190 0 0 1 448,26 L445,60 A150,150 0 0 0 302,170 Z" fill="var(--red)"/>
    </svg>
    <div class="brand"><span class="brand__mark"></span>KVL</div>
    <h1 class="cover__title"><span class="red">YOUR BRUSH</span><span class="grey">SOLUTION</span></h1>
    <p class="cover__tagline">DESIGNING THE FUTURE SINCE 1908</p>
    <p class="url">www.korvalbristle.com</p>
  </section>

  <section class="slide slide--family">
    <header class="slide-header">
      <h2 class="slide-header__title"><span class="red">A FAMILY</span> <span class="grey">COMPANY</span></h2>
      <div class="slide-header__rule"></div>
      <div class="brand"><span class="brand__mark"></span>KVL</div>
    </header>
    <p class="family__intro">Driving excellence and keeping on developing innovative products thanks to our incredible <strong>Team of Talents</strong>.</p>
    <div class="family__band"></div>
    <div class="family__photo" role="img" aria-label="Group photo of the company team in front of the factory building"></div>
    <div class="family__footer"><span class="tab"></span><p class="url">www.korvalbristle.com</p><span class="rule"></span></div>
  </section>

  <section class="slide slide--heritage">
    <header class="slide-header">
      <h2 class="slide-header__title"><span class="red">OUR STRONG</span> <span class="grey">HERITAGE</span></h2>
      <div class="slide-header__rule"></div>
      <div class="brand"><span class="brand__mark"></span>KVL</div>
    </header>
    <div class="heritage__map" role="img" aria-label="Faint world map behind the timeline"></div>
    <svg class="timeline" width="534" height="301" viewBox="0 0 534 301">
      <path d="M0,142 C25,142 28,165 53,165 C78,165 78,142 103,142 C128,142 128,165 153,165 C178,165 178,142 203,142 C228,142 228,165 253,165 C278,165 278,142 303,142 C328,142 328,165 353,165 C378,165 378,142 403,142 C428,142 428,165 453,165 C478,165 478,142 503,142 C520,142 528,152 534,158" fill="none" stroke="var(--red)" stroke-width="5" stroke-linecap="round"/>
      <g stroke="#b5b5b5" stroke-width="2.5">
        <line x1="103" y1="96" x2="103" y2="142"/><line x1="203" y1="96" x2="203" y2="142"/><line x1="303" y1="96" x2="303" y2="142"/><line x1="403" y1="96" x2="403" y2="142"/><line x1="503" y1="96" x2="503" y2="142"/>
        <line x1="53" y1="165" x2="53" y2="212"/><line x1="153" y1="165" x2="153" y2="212"/><line x1="253" y1="165" x2="253" y2="212"/><line x1="353" y1="165" x2="353" y2="212"/><line x1="453" y1="165" x2="453" y2="212"/>
      </g>
      <g fill="#fff" stroke="#c4c4c4" stroke-width="2.5">
        <circle cx="103" cy="96" r="7"/><circle cx="203" cy="96" r="7"/><circle cx="303" cy="96" r="7"/><circle cx="403" cy="96" r="7"/><circle cx="503" cy="96" r="7"/>
        <circle cx="53" cy="212" r="7"/><circle cx="153" cy="212" r="7"/><circle cx="253" cy="212" r="7"/><circle cx="353" cy="212" r="7"/><circle cx="453" cy="212" r="7"/>
      </g>
      <g fill="var(--red)">
        <circle cx="103" cy="96" r="3.5"/><circle cx="203" cy="96" r="3.5"/><circle cx="303" cy="96" r="3.5"/><circle cx="403" cy="96" r="3.5"/><circle cx="503" cy="96" r="3.5"/>
        <circle cx="53" cy="212" r="3.5"/><circle cx="153" cy="212" r="3.5"/><circle cx="253" cy="212" r="3.5"/><circle cx="353" cy="212" r="3.5"/><circle cx="453" cy="212" r="3.5"/>
        <circle cx="53" cy="166" r="2.5"/><circle cx="153" cy="166" r="2.5"/><circle cx="253" cy="166" r="2.5"/><circle cx="353" cy="166" r="2.5"/><circle cx="453" cy="166" r="2.5"/>
      </g>
      <text class="year" x="36" y="145">1662</text>
      <text class="year" x="87" y="165">1908</text>
      <text class="year" x="138" y="150">2012</text>
      <text class="year" x="188" y="166">2014</text>
      <text class="year" x="238" y="148">2018</text>
      <text class="year" x="288" y="165">2019</text>
      <text class="year" x="387" y="166">2020</text>
      <text class="year" x="437" y="148">2021</text>
      <text class="year" x="490" y="169">2023</text>
    </svg>
    <div class="milestone" style="left:103px;top:50px"><div class="milestone__photo" role="img" aria-label="Historic workshop sign"></div></div>
    <div class="milestone milestone__name" style="left:203px;top:58px"><span class="sq"></span>KVL → KVL</div>
    <div class="milestone milestone__partner" style="left:322px;top:60px">NEXACUBE</div>
    <div class="milestone" style="left:400px;top:52px"><div class="milestone__badge-blue"></div></div>
    <div class="milestone milestone__ready" style="left:501px;top:50px">Ready for the next 115 years</div>
    <div class="milestone" style="left:53px;top:222px"><div class="milestone__brushes" role="img" aria-label="Antique paint brushes"></div></div>
    <div class="milestone milestone__name" style="left:153px;top:236px">StreamHub</div>
    <div class="milestone milestone__name" style="left:253px;top:236px"><span class="sq"></span>KVL 110</div>
    <div class="milestone milestone__name" style="left:353px;top:236px">PhotoGram</div>
    <div class="milestone" style="left:453px;top:226px"><div class="milestone__badge-ring"></div></div>
    <div class="slide-footer"><span class="tab"></span><p class="url">www.korvalbristle.com</p><span class="rule"></span></div>
  </section>

  <section class="slide slide--world">
    <header class="slide-header">
      <h2 class="slide-header__title"><span class="red">OUR JOURNEY</span> <span class="grey">AROUND THE WORLD</span></h2>
      <div class="slide-header__rule"></div>
      <div class="brand"><span class="brand__mark"></span>KVL</div>
    </header>
    <ul class="facts">
      <li class="fact"><div class="fact__check"><span><svg width="11" height="9" viewBox="0 0 11 9"><path d="M1,4.5 L4,7.5 L10,1" fill="none" stroke="#fff" stroke-width="2"/></svg></span></div><div class="fact__pill">Constantly growing customer base: 5,000+</div></li>
      <li class="fact"><div class="fact__check"><span><svg width="11" height="9" viewBox="0 0 11 9"><path d="M1,4.5 L4,7.5 L10,1" fill="none" stroke="#fff" stroke-width="2"/></svg></span></div><div class="fact__pill">Our products are sold in 75+ countries</div></li>
      <li class="fact"><div class="fact__check"><span><svg width="11" height="9" viewBox="0 0 11 9"><path d="M1,4.5 L4,7.5 L10,1" fill="none" stroke="#fff" stroke-width="2"/></svg></span></div><div class="fact__pill">2 production sites in EU (Italy &amp; Romania)</div></li>
    </ul>
    <div class="world__map" role="img" aria-label="Grey world map"></div>
    <div class="slide-footer"><span class="tab"></span><p class="url">www.korvalbristle.com</p><span class="rule"></span></div>
  </section>

</main>
</body>
</html>
```